PowerPoint Template Design for Quarry Lending

Design a PowerPoint template for Quarry Lending, tailored for presentations to sophisticated mortgage servicing investors. The template should reflect a high level of professionalism, with a clean and modern aesthetic that resonates with an informed and discerning audience. The design must effectively integrate Quarry Lending's branding elements, ensuring a coherent visual narrative that reinforces our reputation for expertise and reliability in the mortgage servicing sector.

```html
<!DOCTYPE html>
<html lang="en">
<head>
<meta charset="utf-8">
<title>Quarry Lending — Presentation Template</title>
<link href="https://fonts.googleapis.com/css2?family=Playfair+Display:wght@700;800;900&family=Oswald:wght@500;600&family=Plus+Jakarta+Sans:wght@400;500;600&display=swap" rel="stylesheet">
<style>
  :root {
    --cream: #fcf4cf;
    --gold: #dfb240;
    --navy: #252050;
    --ink: #0f0d1f;
    --page: #ffffff;
    --serif: "Playfair Display", Georgia, serif;
    --condensed: "Oswald", "Arial Narrow", sans-serif;
    --sans: "Plus Jakarta Sans", Arial, sans-serif;
  }
  * { box-sizing: border-box; margin: 0; padding: 0; }
  html, body { width: 1200px; height: 1200px; overflow: hidden; background: var(--page); }
  .canvas { position: relative; width: 1200px; height: 1200px; }
  .slide { position: absolute; width: 464px; height: 261px; overflow: hidden; }
  .col-left { left: 102.5px; }
  .col-right { left: 639px; }
  .bg-cream { background: var(--cream); }
  .bg-gold { background: var(--gold); }
  .bg-navy { background: var(--navy); }
  .abs { position: absolute; }

  .brand { position: absolute; left: 27px; top: 44px; display: flex; align-items: center; gap: 10px; }
  .brand-dot { width: 16px; height: 16px; border-radius: 50%; background: var(--navy); }
  .brand-name { font-family: var(--serif); font-weight: 900; font-size: 38px; color: var(--gold); line-height: 1; }

  .cover-title { left: 27px; top: 141px; font-family: var(--serif); font-weight: 900; font-size: 22.5px; color: var(--ink); letter-spacing: 0.2px; white-space: nowrap; }
  .cover-band { position: absolute; left: 0; top: 183px; width: 100%; height: 78px; background: var(--gold); }
  .band-link { position: absolute; left: 27px; top: 31px; font-family: var(--condensed); font-weight: 500; font-variant: small-caps; font-size: 12.5px; color: var(--navy); text-decoration: underline; text-underline-offset: 2px; letter-spacing: 0.3px; }
  .band-arrow { position: absolute; left: 399px; top: 31px; }

  .overview-title { left: 27px; top: 150px; font-family: var(--serif); font-weight: 900; font-size: 30px; line-height: 32px; color: var(--navy); }
  .overview-sub { left: 27px; top: 223px; font-family: var(--condensed); font-weight: 500; font-variant: small-caps; font-size: 10.5px; color: var(--navy); letter-spacing: 0.2px; }

  .centre-title { left: 0; width: 100%; text-align: center; font-family: var(--serif); font-weight: 900; }
  .revamp { top: 72px; font-size: 34px; line-height: 39px; color: var(--navy); text-decoration: underline; text-decoration-thickness: 2px; text-underline-offset: 3px; }
  .stats-title { top: 31px; font-size: 30px; line-height: 32px; color: var(--gold); }

  .stat { position: absolute; top: 152px; width: 170px; text-align: center; font-family: var(--sans); color: var(--gold); }
  .stat-head { font-weight: 600; font-size: 11.5px; line-height: 15px; text-decoration: underline; text-underline-offset: 2px; }
  .stat-body { margin-top: 7px; font-size: 8.6px; line-height: 11.5px; }

  .usa-title { left: 26px; top: 90px; font-family: var(--serif); font-weight: 900; font-size: 25px; line-height: 27px; color: var(--gold); }
  .feature { position: absolute; width: 112px; font-family: var(--sans); color: var(--gold); }
  .feature-num { font-family: var(--serif); font-weight: 800; font-size: 12.5px; text-decoration: underline; text-underline-offset: 2px; }
  .feature-head { margin-top: 12px; font-weight: 600; font-size: 9.6px; line-height: 12.5px; }
  .feature-body { margin-top: 6px; font-size: 7px; line-height: 9.6px; }

  .concepts-title { left: 26px; top: 27px; font-family: var(--serif); font-weight: 900; font-size: 30px; line-height: 31px; color: var(--gold); }
  .concept { position: absolute; top: 140px; width: 130px; font-family: var(--sans); color: var(--gold); }
  .concept-num { font-family: var(--serif); font-weight: 800; font-size: 17px; text-decoration: underline; text-underline-offset: 2px; }
  .concept-head { margin-top: 8px; font-weight: 600; font-size: 11.5px; line-height: 15px; }
  .concept-body { margin-top: 4px; font-size: 8.8px; line-height: 11.5px; }

  .quote-mark { left: 21px; top: 16px; font-family: var(--serif); font-weight: 900; font-size: 34px; color: var(--navy); line-height: 1; }
  .quote-text { left: 38px; top: 27px; width: 400px; font-family: var(--serif); font-weight: 800; font-size: 22px; line-height: 31px; color: var(--navy); }
  .quote-close { font-size: 28px; vertical-align: 6px; line-height: 0; }
  .quote-author { left: 38px; top: 224px; font-family: var(--sans); font-weight: 600; font-size: 11px; color: var(--navy); }
</style>
</head>
<body>
<main class="canvas">

  <section class="slide col-left bg-cream" style="top:80.6px">
    <div class="brand"><span class="brand-dot"></span><span class="brand-name">Quarry Lending</span></div>
    <h1 class="abs cover-title">MORTGAGE SERVICES INVESTORS</h1>
    <div class="cover-band">
      <span class="band-link">Trustworthy Mortgage Services Investors</span>
      <svg class="band-arrow" width="35" height="16" viewBox="0 0 35 16" aria-hidden="true">
        <path d="M1 8 H33 M25 1.5 L33 8 L25 14.5" fill="none" stroke="var(--navy)" stroke-width="1.8" stroke-linecap="round" stroke-linejoin="round"/>
      </svg>
    </div>
  </section>

  <section class="slide col-left bg-cream" style="top:344px">
    <div class="brand"><span class="brand-dot"></span><span class="brand-name">Quarry Lending</span></div>
    <h2 class="abs overview-title">MORTGAGE SERVICES<br>OVERVIEW</h2>
    <p class="abs overview-sub">Our Mortgage Service: Empowering You to Own Your Dream Home</p>
  </section>

  <section class="slide col-left bg-gold" style="top:608px">
    <h2 class="abs centre-title revamp">REVAMP YOUR<br>MORTGAGE<br>EXPERIENCE</h2>
  </section>

  <section class="slide col-left bg-navy" style="top:873px">
    <h2 class="abs centre-title stats-title">COMPARISON OF<br>STATISTICS</h2>
    <div class="stat" style="left:44px">
      <p class="stat-head">90% customer<br>satisfaction rate</p>
      <p class="stat-body">Our customers love our mortgage services because we put their needs first.</p>
    </div>
    <div class="stat" style="left:263px; width:172px">
      <p class="stat-head">30+ years of experience<br>in mortgage service</p>
      <p class="stat-body">We have been providing mortgage services for over 30 years, so you can trust us to know what we're doing.</p>
    </div>
  </section>

  <section class="slide col-right bg-navy" style="top:213px">
    <h2 class="abs usa-title">MORTGAGE<br>SERVICES IN<br>USA</h2>
    <div class="feature" style="left:210px; top:43px">
      <p class="feature-num">01</p>
      <p class="feature-head">Lowest Interest Rates Available</p>
      <p class="feature-body">We offer the lowest interest rates available in the market.</p>
    </div>
    <div class="feature" style="left:334px; top:43px">
      <p class="feature-num">02</p>
      <p class="feature-head">Custom Mortgage Packages for All</p>
      <p class="feature-body">Our custom mortgage packages are tailored to fit your individual needs.</p>
    </div>
    <div class="feature" style="left:210px; top:149px">
      <p class="feature-num">03</p>
      <p class="feature-head">Mortgage Refinancing Available</p>
      <p class="feature-body">Refinance your home with ease with our mortgage refinancing services.</p>
    </div>
    <div class="feature" style="left:334px; top:149px">
      <p class="feature-num">04</p>
      <p class="feature-head">Fast and Secure Online Applications</p>
      <p class="feature-body">Get approved in minutes with our online application process.</p>
    </div>
  </section>

  <section class="slide col-right bg-navy" style="top:478px">
    <h2 class="abs concepts-title">3 KEY CONCEPTS FOR<br>MORTGAGES</h2>
    <div class="concept" style="left:26px">
      <p class="concept-num">01</p>
      <p class="concept-head">Flexible Mortgage<br>Options</p>
      <p class="concept-body">Our mortgage service provides different options to suit a variety of customer needs.</p>
    </div>
    <div class="concept" style="left:164px">
      <p class="concept-num">02</p>
      <p class="concept-head">Expert Mortgage<br>Advice</p>
      <p class="concept-body">Our team of mortgage experts provide tailored advice to help you make informed decisions.</p>
    </div>
    <div class="concept" style="left:301px">
      <p class="concept-num">03</p>
      <p class="concept-head">Efficient Mortgage<br>Process</p>
      <p class="concept-body">Our streamlined mortgage process ensures fast &amp; efficient service for our customers.</p>
    </div>
  </section>

  <section class="slide col-right bg-gold" style="top:742.5px">
    <span class="abs quote-mark" aria-hidden="true">&ldquo;</span>
    <blockquote class="abs quote-text">I FOUND HARBOR HOME LOANS ON QUARRY LENDING AND CONTACTED DANA WHITFIELD THROUGH HARBOR&rsquo;S WEBSITE. DANA WAS INCREDIBLY RESPONSIVE. <span class="quote-close">&rdquo;</span></blockquote>
    <p class="abs quote-author">- Sam Carter</p>
  </section>

</main>
</body>
</html>
```